Eyecatching website design for commercial lighting business

This contest is all about the graphic design aspect. We need a striking website design for a commercial lighting company. We want something really eye catching to introduce people to our range of induction and LED lights which save businesses money on maintenance and electricity costs.

To be successful in this contest you will need to provide a design and pictures for the pages listed below.

We are using the platform talvo.com.au and you can see the attached template which everything will be loaded into so we just need HTML files which we can upload and we can do everything else from Talvo.

The final design should be strong and clean and use the colours and textures in the attached business card file.

Detailed requirements:

Please see attached screenshot of the website template, all we need is a fantastic graphic design and improvement/ incorporation of our logo for the following pages
Page Headings:
1. Home
About Us, Contact Us, snapshot of and link to Blog

Each of the below pages will have several paragraphs of text followed by a list of suitable products which is generated from our product catalogue.

2. Car Park Lighting
3. Educational Lighting
4. Hospitality Lighting
5. Office & Shop Lighting
6. Warehouse Lighting

Some of the website we have seen which are similar in nature are:
http://www.quorbenlamps.com.au/
http://www.yimra.com/
http://www.brightvane.net/commercial-led
but we really want a modern, eye catching and memorable design

Some of the designs built on Talvo that we like are:

http://www.harbourmarket.com.au/
http://www.tacklebay.com.au/
http://www.wenbrook.com.au/

I've also uploaded a couple of photos that we love. We'd like something similar for each industry.

Target Market(s)

Company Owners, Maintenance & Facilities Managers, Electrical Contractors

Industry/Entity Type

Electrical

Coding

Coded - Design and coding required

Number of Pages Required

5+ page

Font styles to use
Sans Serif

Colors
33a6d7
ec1f27

Requirements
Must have
• -Must scale to mobile
• -HTML coded files need to be provided (HTML Bootstrap)
Nice to have
• -Prefer incorporation of our logo into header bar
• -Design of 2-3 advertising banners which can be displayed on the home page
• -Prominent call to action button towards top of page 'Get a quote' or similar
• -Grid based design HTML Bootstrap

```html
<!DOCTYPE html>
<html lang="en">
<head>
<meta charset="utf-8">
<title>Harlan &amp; Pike Lighting</title>
<link href="https://fonts.googleapis.com/css2?family=Open+Sans:wght@400;600;700&family=Oswald:wght@400;500&display=swap" rel="stylesheet">
<style>
:root{
  --red:#d8141c;
  --red-dark:#a90e14;
  --blue:#33a6d7;
  --ink:#333;
  --muted:#777;
  --dark:#1e1f22;
  --darker:#141517;
  --panel:#263039;
  --light:#f4f4f4;
  --white:#fff;
}
*{box-sizing:border-box;margin:0;padding:0}
html,body{width:678px;height:1200px;overflow:hidden}
body{font-family:"Open Sans",Arial,sans-serif;color:var(--ink);background:var(--white);font-size:7px;line-height:1.45}
.page{width:678px;height:1200px;position:relative}

/* header */
.site-header{height:78px;display:flex;justify-content:space-between;align-items:flex-start;padding:12px 42px 0}
.brand{display:flex;align-items:center;gap:6px;background:var(--dark);padding:8px 10px;height:32px}
.brand-mark{width:12px;height:12px;background:var(--red)}
.brand-name{font-family:"Oswald",sans-serif;font-size:11px;color:var(--white);letter-spacing:.5px}
.search{display:flex;margin-top:16px}
.search span{width:92px;height:18px;border:1px solid #ccc;font-size:6px;color:#999;padding:4px 6px}
.search i{width:18px;height:18px;background:#555}

/* hero */
.hero{position:absolute;top:78px;left:0;width:678px;height:282px;background:linear-gradient(180deg,#c9121a,#e52029 60%,#b80f16);}
.main-nav{position:absolute;top:20px;left:52px;width:574px;height:22px;background:var(--red-dark);display:flex;padding-left:12px}
.main-nav a{color:var(--white);text-decoration:none;font-size:8px;padding:5px 20px;font-weight:600}
.main-nav a.active{background:var(--red)}
.hero-photo{position:absolute;top:42px;left:52px;width:574px;height:200px;background:radial-gradient(circle at 45% 45%,#f7c47a 0,#c06a2a 18%,#4a1e14 45%,#1c0e0c 75%)}
.hero-copy{position:absolute;top:105px;left:0;width:678px;text-align:center;color:var(--white);font-family:"Oswald",sans-serif;font-size:13px;line-height:1.25;letter-spacing:.3px}
.hero-btn{display:inline-block;margin-top:10px;background:var(--red);color:var(--white);font-family:"Open Sans",sans-serif;font-size:6.5px;font-weight:700;padding:5px 12px}
.arrow{position:absolute;top:130px;width:20px;height:20px;border-radius:50%;background:var(--white)}
.arrow svg{width:20px;height:20px}
.arrow.left{left:52px}.arrow.right{left:606px}

/* intro */
.section-title{font-family:"Oswald",sans-serif;color:var(--red);font-size:14px;font-weight:500;text-align:center;letter-spacing:.4px}
.intro{position:absolute;top:380px;left:0;width:678px;height:210px}
.intro .section-title{margin-top:62px;margin-top:0}
.video{position:absolute;top:34px;left:74px;width:160px;height:120px;border:4px solid var(--white);box-shadow:0 1px 4px rgba(0,0,0,.3);background:linear-gradient(180deg,#1d2438,#5a3a28 65%,#8a5a32)}
.video .play{position:absolute;left:62px;top:42px;width:28px;height:28px;border-radius:50%;background:var(--red)}
.intro-text{position:absolute;top:40px;left:346px;width:264px;color:var(--muted);font-size:6.5px}
.intro-text p{margin-bottom:8px}
.btn{display:inline-block;background:var(--red);color:var(--white);font-weight:700;font-size:7px;padding:6px 14px}
.intro .btn{position:absolute;top:148px;left:394px}

/* blogs */
.blogs{position:absolute;top:586px;left:0;width:678px;height:198px;background:linear-gradient(180deg,#11161c,#2b3a47 50%,#151a20)}
.blogs .section-title{color:var(--white);margin-top:16px}
.post{position:absolute;top:52px;width:228px;display:flex;gap:8px}
.post.one{left:112px}.post.two{left:354px}
.post-img{width:110px;height:74px;flex:none}
.post.one .post-img{background:linear-gradient(180deg,#0d1a33,#2f4f86 60%,#5c6fa0)}
.post.two .post-img{background:linear-gradient(180deg,#4a3326,#8a5a3c 55%,#3a2a22)}
.post h3{color:var(--white);font-size:7px;font-weight:700}
.post .date{color:#9aa;font-size:5.5px;margin-bottom:4px}
.post p{color:#c9cfd4;font-size:5.5px}
.post .more{color:var(--red);font-size:5.5px;font-weight:700;margin-top:4px}
.dots{position:absolute;top:150px;left:326px;display:flex;gap:5px}
.dots i{width:10px;height:10px;border-radius:50%;background:#4b5560}

/* solutions */
.solutions{position:absolute;top:792px;left:0;width:678px;height:206px}
.solutions .lead{text-align:center;color:var(--muted);font-size:6px;margin-top:2px}
.cards{display:flex;gap:10px;position:absolute;top:34px;left:52px}
.card{width:136px}
.card-img{height:80px}
.c1{background:linear-gradient(180deg,#4a4f58,#9aa3ad 50%,#5b616a)}
.c2{background:linear-gradient(180deg,#c9d6e2,#7f93a8 60%,#3c4a5a)}
.c3{background:linear-gradient(180deg,#6a4a32,#b58a5c 55%,#4d3626)}
.c4{background:linear-gradient(180deg,#dfe6ec,#a8b7c4 60%,#6d7e8c)}
.card h4{color:var(--red);font-size:7.5px;font-weight:700;margin:8px 0 3px}
.card p{color:var(--muted);font-size:5.5px}
.card .more{color:var(--red);font-size:5.5px;font-weight:700;margin-top:4px}

/* footer */
.site-footer{position:absolute;top:1000px;left:0;width:678px;height:172px;background:var(--dark);padding:22px 52px 0;display:flex;gap:20px}
.col{width:128px;color:#9aa0a6;font-size:5.5px}
.col.news{width:150px}
.col h5{color:var(--white);font-size:8px;font-weight:600;margin-bottom:4px}
.col .rule{height:1px;background:#3a3d42;margin-bottom:8px}
.col li{list-style:none;line-height:1.7}
.field{height:16px;background:var(--white);margin:6px 0 8px}
.col .btn{font-size:6px;padding:4px 10px}
.bottom-bar{position:absolute;top:1172px;left:0;width:678px;height:28px;background:var(--darker);display:flex;justify-content:space-between;align-items:center;padding:0 52px;color:#888;font-size:5.5px}
.social{display:flex;align-items:center;gap:5px;color:#bbb}
.social i{width:8px;height:8px;background:var(--red)}
</style>
</head>
<body>
<div class="page">
  <header class="site-header">
    <div class="brand"><span class="brand-mark"></span><span class="brand-name">Harlan &amp; Pike</span></div>
    <div class="search"><span>Search</span><i></i></div>
  </header>

  <section class="hero">
    <div class="hero-photo" role="img" aria-label="Close-up of glowing induction light bulbs"></div>
    <nav class="main-nav">
      <a class="active">Home</a><a>About us</a><a>Products</a><a>Blog</a><a>Contact us</a>
    </nav>
    <div class="hero-copy">INDUCTION LIGHTING<br>SAVE YOU UP TO 85% IN ENERGY COST<br><span class="hero-btn">CONTACT US</span></div>
    <span class="arrow left"><svg viewBox="0 0 20 20"><path d="M12 5l-5 5 5 5" fill="none" stroke="#999" stroke-width="2"/></svg></span>
    <span class="arrow right"><svg viewBox="0 0 20 20"><path d="M8 5l5 5-5 5" fill="none" stroke="#999" stroke-width="2"/></svg></span>
  </section>

  <section class="intro">
    <h2 class="section-title">HARLAN &amp; PIKE BUSINESS SOLUTIONS</h2>
    <div class="video" role="img" aria-label="Video still of a lit building at night"><span class="play"></span></div>
    <div class="intro-text">
      <p>Lorem ipsum is simply dummy text of the printing and typesetting industry. Lorem ipsum has been the industry's standard dummy text ever since the 1500s, when an unknown printer took a galley of type and scrambled it to make a type specimen book. It has survived not only five centuries.</p>
      <p>It has also leapt into electronic typesetting, remaining essentially unchanged. It was popularised in the 1960s with the release of sheets containing Lorem Ipsum passages.</p>
    </div>
    <span class="btn">VIEW MORE</span>
  </section>

  <section class="blogs">
    <h2 class="section-title">OUR BLOGS</h2>
    <article class="post one">
      <div class="post-img" role="img" aria-label="Lit sports court at night"></div>
      <div><h3>LOREM IPSUM IS FREE</h3><div class="date">15 January 2015, 3 comments</div><p>Lorem ipsum is simply dummy text of the printing and typesetting industry. Lorem ipsum has been the standard.</p><div class="more">READ MORE &gt;</div></div>
    </article>
    <article class="post two">
      <div class="post-img" role="img" aria-label="Warmly lit hotel lounge"></div>
      <div><h3>LOREM IPSUM IS FREE</h3><div class="date">15 January 2015, 3 comments</div><p>Lorem ipsum is simply dummy text of the printing and typesetting industry. Lorem ipsum has been the standard.</p><div class="more">READ MORE &gt;</div></div>
    </article>
    <div class="dots"><i></i><i></i></div>
  </section>

  <section class="solutions">
    <h2 class="section-title">LIGHTING SOLUTIONS</h2>
    <p class="lead">Lorem ipsum is simply dummy text of the printing and typesetting industry.</p>
    <div class="cards">
      <div class="card"><div class="card-img c1" role="img" aria-label="Lit underground car park"></div><h4>CAR PARK LIGHTING</h4><p>Lorem ipsum is simply dummy text of the printing and typesetting industry.</p><div class="more">READ MORE &gt;</div></div>
      <div class="card"><div class="card-img c2" role="img" aria-label="Bright school hallway"></div><h4>EDUCATIONAL LIGHTING</h4><p>Lorem ipsum is simply dummy text of the printing and typesetting industry.</p><div class="more">READ MORE &gt;</div></div>
      <div class="card"><div class="card-img c3" role="img" aria-label="Hotel room with warm lighting"></div><h4>HOSPITALITY LIGHTING</h4><p>Lorem ipsum is simply dummy text of the printing and typesetting industry.</p><div class="more">READ MORE &gt;</div></div>
      <div class="card"><div class="card-img c4" role="img" aria-label="Open plan office with ceiling lights"></div><h4>OFFICE LIGHTING</h4><p>Lorem ipsum is simply dummy text of the printing and typesetting industry.</p><div class="more">READ MORE &gt;</div></div>
    </div>
  </section>

  <footer class="site-footer">
    <div class="col"><h5>ABOUT US</h5><div class="rule"></div><p>Lorem ipsum is simply dummy text of the printing and typesetting industry. Lorem ipsum has been the industry's standard dummy text.</p></div>
    <div class="col"><h5>CONTACT US</h5><div class="rule"></div><ul><li>12 Ferris Lane</li><li>Northgate NSW 2000</li><li>Phone: 02 5550 1234</li><li>info@harlanpike.com</li></ul></div>
    <div class="col"><h5>SUPPORT LINKS</h5><div class="rule"></div><ul><li>Home</li><li>About Us</li><li>Products</li><li>Blog</li><li>Contact Us</li></ul></div>
    <div class="col news"><h5>NEWSLETTER SIGN UP</h5><div class="rule"></div><p>Please sign up here for news</p><div class="field"></div><span class="btn">SUBSCRIBE</span></div>
  </footer>
  <div class="bottom-bar">
    <span>© 2015 Harlan &amp; Pike. All rights reserved. Terms of Use</span>
    <span class="social">Social Media <i></i><i></i><i></i><i></i><i></i></span>
  </div>
</div>
</body>
</html>
```